Design an Amazing Mailer for our Company

Using the copy and image ideas provided, create a 2-sided 12x15 mailer for our direct mail and print company to drive new customers to us. Be creative but keep the themes we want to go with in mind. Copy and sample images provided on the included file.

Target Market(s)

Small local businesses in our community

Industry/Entity Type

Direct Mail and Printing Company

Font styles to use
Serif
Sans Serif

Colors
0054AA
0677BA
7BADD7
CADEEF
E8F1F8
0094D4
00A9DD
6FCCEA
C7EBF8
E9F6FB

```html
<!DOCTYPE html>
<html lang="en">
<head>
<meta charset="utf-8">
<title>Maple Street Mailing – Two-Sided Mailer</title>
<link rel="stylesheet" href="https://fonts.googleapis.com/css2?family=Poppins:ital,wght@0,400;0,600;0,700;1,700&family=Open+Sans:wght@400&display=swap">
<style>
  :root {
    --navy: #24215f;
    --white: #ffffff;
    --ink: #111111;
    --stage: #e6e6ee;
    --hero-tint: #f1f1f5;
    --sample-orange: #b8742a;
    --sample-olive: #6d6a2a;
    --sample-pink: #e7d6ea;
    --sample-gray: #d9d4cf;
    --sample-green: #4f5a43;
    --sample-dark: #3a3340;
    --sample-red: #a4563a;
    --mark-blue: #2a5aa8;
  }
  * { margin: 0; padding: 0; box-sizing: border-box; }
  html, body { width: 1200px; height: 1200px; overflow: hidden; }
  body { background: var(--stage); position: relative; font-family: "Poppins", sans-serif; color: var(--ink); }

  .mailer-side { position: absolute; left: 265px; width: 670px; height: 535px; background: var(--white); overflow: hidden; }
  .side-front { top: 50px; }
  .side-back { top: 605px; }

  .hero-backdrop { position: absolute; left: 0; top: 0; width: 100%; height: 269px; background: linear-gradient(90deg, var(--hero-tint) 0%, var(--white) 85%); }

  .brand-mark { position: absolute; display: flex; align-items: center; gap: 8px; color: var(--navy); font-family: "Poppins", sans-serif; font-weight: 700; font-size: 15px; line-height: 1.15; width: 130px; }
  .brand-mark .square { width: 16px; height: 16px; background: var(--navy); flex: none; }
  .front-mark { left: 512px; top: 105px; }
  .back-mark { left: 528px; top: 105px; }

  .front-kicker { position: absolute; left: 34px; top: 30px; font-weight: 600; font-size: 18px; letter-spacing: 0.2px; }
  .front-headline { position: absolute; left: 34px; top: 82px; font-weight: 700; font-style: italic; font-size: 25px; line-height: 1.2; }
  .front-intro { position: absolute; left: 34px; top: 160px; width: 560px; font-size: 11.3px; line-height: 1.3; }
  .front-intro p { margin-bottom: 11px; }

  .services-band { position: absolute; left: 0; top: 269px; width: 100%; height: 159px; background: var(--navy); color: var(--white); padding: 15px 34px; }
  .services-band h3 { font-weight: 600; font-size: 13px; margin-bottom: 3px; }
  .services-band li { list-style: none; font-size: 11.3px; line-height: 18.8px; }
  .services-band li::before { content: "▪ "; }

  .front-offer { position: absolute; left: 34px; top: 446px; width: 610px; }
  .front-offer h4 { font-weight: 600; font-size: 13.5px; margin-bottom: 8px; }
  .front-offer p { font-size: 11.3px; line-height: 1.3; }

  .back-panel { position: absolute; left: 0; top: 0; width: 478px; height: 398px; background: var(--navy); color: var(--white); padding: 36px 34px 0; }
  .back-headline { font-weight: 600; font-size: 27px; line-height: 1.2; }
  .back-answer { font-weight: 700; font-style: italic; font-size: 30px; line-height: 1.2; margin: 4px 0 12px; }
  .back-copy { font-family: "Open Sans", sans-serif; font-size: 10.2px; line-height: 13.3px; width: 416px; }
  .back-copy p { margin-bottom: 13px; }

  .sample { position: absolute; }
  .sample-halloween { left: 34px; top: 379px; width: 108px; height: 139px; background: linear-gradient(160deg, var(--sample-orange), var(--sample-olive)); }
  .sample-team { left: 160px; top: 462px; width: 70px; height: 44px; }
  .sample-save-date { left: 248px; top: 430px; width: 127px; height: 88px; background: linear-gradient(180deg, #f6eef6, var(--sample-pink)); border: 1px solid #ddd; }
  .sample-summit { left: 384px; top: 401px; width: 78px; height: 117px; background: linear-gradient(180deg, var(--sample-gray), #b9a89a); border: 1px solid #ddd; }
  .sample-magazine { left: 475px; top: 401px; width: 85px; height: 117px; background: linear-gradient(180deg, #6e7a68, var(--sample-green)); }
  .sample-poster { left: 572px; top: 401px; width: 78px; height: 117px; background: linear-gradient(180deg, #5a5566, var(--sample-dark)); }
  .sample-sale { left: 572px; top: 279px; width: 78px; height: 110px; background: linear-gradient(180deg, #c9873e, var(--sample-red)); }
</style>
</head>
<body>

<section class="mailer-side side-front">
  <div class="hero-backdrop" role="img" aria-label="Soft decorative backdrop behind the headline"></div>

  <h2 class="front-kicker">WHAT HAPPENS IN BURBANK (SHOULD) STAY IN BURBANK</h2>
  <h1 class="front-headline">You’ve got a neighbor in<br>the direct mail business.</h1>

  <div class="brand-mark front-mark"><span class="square"></span><span>Maple Street Mailing</span></div>

  <div class="front-intro">
    <p>For 75 years, Maple Street Mailing has been serving our<br>community- from large studios to small mom-and-pop stores.</p>
    <p>We live here, too!</p>
    <p>As a local family, we ascribe to the values that make our community special- that small town<br>feel with big city services- focused on keeping us all connected.</p>
  </div>

  <div class="services-band">
    <h3>WHAT WE DO:</h3>
    <ul>
      <li>Direct Mail/Marketing</li>
      <li>Mailing for Union Pension, Insurance, and Healthcare Notices &amp; Membership Voting Materials</li>
      <li>Nonprofit Mailing</li>
      <li>Political and Community Campaign Mailing</li>
      <li>City and Government Mailing</li>
      <li>Fulfillment Services</li>
    </ul>
  </div>

  <div class="front-offer">
    <h4>*Green and Union options available</h4>
    <p>Mention this mailer and get a $50 Gift Card to Rosa’s or Roasting the Bean on your first Order of $2500 or more; Get a $100 Gift Card to Rosa’s or Hilltop Market on your first order of $5,000 or more.</p>
  </div>
</section>

<section class="mailer-side side-back">
  <div class="back-panel">
    <h2 class="back-headline">Remember great customer<br>service?</h2>
    <p class="back-answer">We do</p>
    <div class="back-copy">
      <p>We don’t provide a cookie-cutter mail service. We focus on helping clients by doing one thing really well—and that’s direct mail. Our team of experts goes through every phase of the direct mail cycle to provide you with better results, higher-value customers, and direct mailing success for years to come. We can design, print, mail, and provide targeted lists, tracking, and analytics. We’re more than a direct mail service provider, we’re your marketing partner!</p>
      <p>When you take these values and wrap them around our commitment to customer satisfaction, you get good old-fashioned customer service that is, sadly, rare these days. At Maple Street Mailing, we view it as an obligation to our customers to go above and beyond to provide them with services that not only meet their needs but exceed their expectations. Our “Make it Right” mentality extends beyond our products and services. Whether it be the timely response to an inquiry, a human answering your call or following-up to ensure your ongoing satisfaction, you can trust that working with MSM will be a rewarding, enjoyable experience on top of an excellent return on your investment.</p>
    </div>
  </div>

  <div class="brand-mark back-mark"><span class="square"></span><span>Maple Street Mailing</span></div>

  <div class="sample sample-sale" role="img" aria-label="Sample mailer: holiday sale flyer"></div>
  <div class="sample sample-halloween" role="img" aria-label="Sample mailer: autumn festival flyer"></div>
  <svg class="sample sample-team" viewBox="0 0 70 44" role="img" aria-label="Client badge placeholder">
    <rect x="0" y="0" width="70" height="44" rx="6" fill="var(--mark-blue)"/>
  </svg>
  <div class="sample sample-save-date" role="img" aria-label="Sample mailer: save the date card"></div>
  <div class="sample sample-summit" role="img" aria-label="Sample mailer: event summit postcard"></div>
  <div class="sample sample-magazine" role="img" aria-label="Sample mailer: magazine cover"></div>
  <div class="sample sample-poster" role="img" aria-label="Sample mailer: film poster"></div>
</section>

</body>
</html>
```